R.L. Penrose Electric Holiday Party Invitation

We need a cohesive, on-brand holiday party invitation suite for R.L. Penrose Electrical Contractors (slogan Driven by Excellence). Design should include: 1) 5x7" invitation (print + digital), 2) matching RSVP card, and 3) raffle ticket.
Use our brand colors (navy, red, white, light gray) and modern professional style with subtle holiday accents.
Event: Thursday, Dec 18 2025 | 6-10 PM | Ravenna Bellhaven, 318 Quillby Ave, Alderbrook NJ 08219.
RSVP by: Dec 1 | Plus one allowed.
Deliver print-ready PDFs + editable source files.

```html
<!DOCTYPE html>
<html lang="en">
<head>
<meta charset="utf-8">
<title>R.L. Penrose Electric Holiday Party Suite</title>
<link href="https://fonts.googleapis.com/css2?family=Noto+Serif:wght@700&family=Poppins:wght@400;500;600;700&family=Great+Vibes&family=Roboto+Slab:wght@700;800&display=swap" rel="stylesheet">
<style>
  :root {
    --navy: #1d2f5f;
    --red: #d41f2b;
    --ticket-red: #ed1c2e;
    --white: #ffffff;
    --paper: #f1f1f2;
    --light-gray: #d9dadc;
    --backdrop: #5c5c5c;
    --ink: #1b1b1f;
  }
  * { box-sizing: border-box; margin: 0; padding: 0; }
  html, body { width: 1200px; height: 987px; overflow: hidden; }
  body {
    background: var(--backdrop);
    font-family: "Poppins", sans-serif;
    position: relative;
  }
  .card {
    position: absolute;
    background: linear-gradient(180deg, var(--white), var(--paper));
    overflow: hidden;
    box-shadow: 0 2px 6px rgba(0,0,0,.25);
  }
  .foliage {
    position: absolute;
    background: radial-gradient(ellipse at center, rgba(190,192,196,.9) 0%, rgba(215,217,220,.6) 45%, rgba(241,241,242,0) 72%);
  }
  .brand {
    position: absolute;
    left: 0; right: 0;
    display: flex; align-items: center; justify-content: center; gap: 6px;
    font-family: "Poppins", sans-serif;
    font-weight: 700;
    color: var(--navy);
    letter-spacing: .08em;
  }
  .brand .dot { background: var(--red); border-radius: 50%; display: inline-block; }
  .centered { position: absolute; left: 0; right: 0; text-align: center; }

  /* Invitation */
  .invitation { left: 105px; top: 138px; width: 396px; height: 554px; }
  .invitation .brand { top: 112px; font-size: 15px; }
  .invitation .brand .dot { width: 9px; height: 9px; }
  .headline { font-family: "Noto Serif", serif; font-weight: 700; line-height: 1; }
  .headline-driven { top: 158px; font-size: 34px; color: var(--red); }
  .headline-driven .by, .rsvp-title .by { font-family: "Great Vibes", cursive; color: var(--navy); font-weight: 400; font-size: 32px; }
  .headline-excellence { top: 192px; font-size: 31px; color: var(--navy); }
  .script-title { top: 224px; font-family: "Great Vibes", cursive; font-size: 38px; color: var(--red); }
  .event-date { top: 288px; display: flex; justify-content: center; align-items: center; gap: 8px;
    font-weight: 600; font-size: 38px; color: var(--red); line-height: 1; }
  .day-badge { width: 48px; height: 48px; border-radius: 50%; background: var(--navy); color: var(--white);
    display: inline-flex; align-items: center; justify-content: center; font-size: 30px; }
  .event-time { position: absolute; left: 80px; width: 242px; top: 339px; height: 24px;
    border-top: 1px solid var(--navy); border-bottom: 1px solid var(--navy);
    display: flex; justify-content: center; align-items: center; gap: 8px;
    font-weight: 600; font-size: 16px; color: var(--navy); }
  .event-time .divider { width: 1px; height: 22px; background: var(--navy); }
  .pin { position: absolute; }
  .venue-name { top: 390px; font-weight: 600; font-size: 13px; color: var(--red); }
  .venue-address { top: 406px; font-weight: 500; font-size: 11px; color: var(--ink); }
  .rsvp-by { top: 430px; font-weight: 600; font-size: 14px; color: var(--red); }
  .rsvp-banner { position: absolute; top: 449px; left: 127px; width: 142px; height: 14px;
    background: var(--navy); color: var(--white); font-size: 9px; text-align: center; line-height: 14px;
    clip-path: polygon(4% 0, 96% 0, 100% 50%, 96% 100%, 4% 100%, 0 50%); }

  /* RSVP card */
  .rsvp-card { left: 559px; top: 149px; width: 554px; height: 396px; }
  .rsvp-card .brand { top: 48px; font-size: 16px; }
  .rsvp-card .brand .dot { width: 9px; height: 9px; }
  .rsvp-title { top: 90px; font-family: "Noto Serif", serif; font-weight: 700; font-size: 40px; color: var(--red); line-height: 1; }
  .rsvp-option { position: absolute; top: 142px; width: 150px; margin-left: -75px; text-align: center;
    font-weight: 600; font-size: 16px; color: var(--navy); }
  .rsvp-option .box { display: block; width: 8px; height: 8px; border: 1px solid var(--ink); margin: 0 auto 6px; }
  .rsvp-deadline { top: 200px; font-weight: 700; font-size: 34px; color: var(--navy); line-height: 1; }
  .name-label { position: absolute; left: 90px; top: 246px; font-weight: 600; font-size: 15px; color: var(--navy); }
  .write-line { position: absolute; left: 90px; width: 373px; height: 1px; background: var(--navy); opacity: .7; }
  .rsvp-address { position: absolute; left: 105px; top: 328px; font-size: 13px; font-weight: 500; color: var(--ink); }
  .rsvp-address strong { color: var(--red); font-weight: 600; }

  /* Raffle ticket */
  .raffle-ticket { left: 571px; top: 615px; width: 435px; height: 158px; }
  .raffle-ticket .brand { top: 26px; width: 294px; right: auto; font-size: 11px; }
  .raffle-ticket .brand .dot { width: 6px; height: 6px; }
  .raffle-title { position: absolute; left: 41px; top: 61px; font-family: "Roboto Slab", serif; font-weight: 800;
    font-size: 27px; color: var(--red); line-height: 1; }
  .raffle-date { position: absolute; left: 41px; top: 98px; display: flex; align-items: center; gap: 3px;
    font-weight: 600; font-size: 14px; color: var(--red); line-height: 1; }
  .raffle-date .day-badge { width: 18px; height: 18px; font-size: 11px; }
  .raffle-time { position: absolute; left: 41px; top: 116px; width: 88px; height: 13px;
    border-top: 1px solid var(--navy); border-bottom: 1px solid var(--navy);
    display: flex; align-items: center; gap: 3px; font-weight: 600; font-size: 8px; color: var(--navy); }
  .raffle-time .divider { width: 1px; height: 11px; background: var(--navy); }
  .raffle-venue { position: absolute; left: 146px; top: 100px; font-size: 7px; line-height: 1.25; color: var(--ink); }
  .raffle-venue strong { display: block; color: var(--red); font-weight: 600; font-size: 8.5px; }
  .ticket-stub { position: absolute; left: 294px; top: 0; width: 141px; height: 158px; background: var(--ticket-red); }
  .stub-field { position: absolute; left: 12px; width: 116px; border-bottom: 1px solid rgba(255,255,255,.6);
    color: var(--white); font-weight: 600; font-size: 8px; padding-bottom: 2px; }
</style>
</head>
<body>

<section class="card invitation" aria-label="Holiday party invitation">
  <div class="foliage" role="img" aria-label="Frosted pine branches with red berries and a silver ornament, top left" style="left:-60px;top:-60px;width:220px;height:230px;"></div>
  <div class="foliage" role="img" aria-label="Frosted pine branches with red berries and a silver ornament, top right" style="right:-60px;top:-60px;width:230px;height:250px;"></div>
  <div class="foliage" role="img" aria-label="Frosted pine branches, bottom left" style="left:-70px;bottom:-60px;width:180px;height:200px;"></div>
  <div class="foliage" role="img" aria-label="Frosted pine branches with red berries, bottom right" style="right:-70px;bottom:-60px;width:190px;height:220px;"></div>

  <div class="brand"><span class="dot"></span>R.L. PENROSE</div>
  <div class="centered headline headline-driven">DRIVEN <span class="by">by</span></div>
  <div class="centered headline headline-excellence">EXCELLENCE</div>
  <div class="centered script-title">Holiday Party</div>
  <div class="centered event-date">DEC <span class="day-badge">18</span> 2025</div>
  <div class="event-time">THURSDAY <span class="divider"></span> 6–10 PM</div>
  <svg class="pin" style="left:192px;top:370px" width="12" height="16" viewBox="0 0 12 16" aria-hidden="true">
    <path d="M6 0C2.7 0 0 2.6 0 5.9 0 10.3 6 16 6 16s6-5.7 6-10.1C12 2.6 9.3 0 6 0z" fill="var(--red)"/>
    <circle cx="6" cy="6" r="2.2" fill="var(--white)"/>
  </svg>
  <div class="centered venue-name">RAVENNA BELLHAVEN</div>
  <div class="centered venue-address">318 Quillby Ave, Alderbrook NJ 08219</div>
  <div class="centered rsvp-by">RSVP BY:</div>
  <div class="rsvp-banner">DEC 1 | PLUS ONE ALLOWED</div>
</section>

<section class="card rsvp-card" aria-label="RSVP card">
  <div class="foliage" role="img" aria-label="Frosted pine branches with red berries and silver ornament, top left" style="left:-60px;top:-60px;width:220px;height:220px;"></div>
  <div class="foliage" role="img" aria-label="Frosted pine branches with red berries and silver ornament, top right" style="right:-60px;top:-60px;width:220px;height:220px;"></div>
  <div class="foliage" role="img" aria-label="Frosted pine branches, bottom left" style="left:-60px;bottom:-60px;width:180px;height:200px;"></div>
  <div class="foliage" role="img" aria-label="Frosted pine branches with red berries, bottom right" style="right:-60px;bottom:-60px;width:190px;height:220px;"></div>

  <div class="brand"><span class="dot"></span>R.L. PENROSE</div>
  <div class="centered rsvp-title">RSVP <span class="by">by</span></div>
  <div class="rsvp-option" style="left:150px"><span class="box"></span>ATTENDING</div>
  <div class="rsvp-option" style="left:277px;width:180px;margin-left:-90px"><span class="box"></span>NOT ATTENDING</div>
  <div class="rsvp-option" style="left:400px"><span class="box"></span>PLUS ONE</div>
  <div class="centered rsvp-deadline">DEC 1</div>
  <div class="name-label">NAME :</div>
  <div class="write-line" style="top:269px"></div>
  <div class="write-line" style="top:299px"></div>
  <svg class="pin" style="left:86px;top:328px" width="12" height="16" viewBox="0 0 12 16" aria-hidden="true">
    <path d="M6 0C2.7 0 0 2.6 0 5.9 0 10.3 6 16 6 16s6-5.7 6-10.1C12 2.6 9.3 0 6 0z" fill="var(--red)"/>
    <circle cx="6" cy="6" r="2.2" fill="var(--white)"/>
  </svg>
  <div class="rsvp-address"><strong>RAVENNA BELLHAVEN</strong> 318 Quillby Ave, Alderbrook NJ 08219</div>
</section>

<section class="card raffle-ticket" aria-label="Raffle ticket">
  <div class="foliage" role="img" aria-label="Frosted pine branches, left edge" style="left:-50px;top:-40px;width:120px;height:240px;"></div>
  <div class="foliage" role="img" aria-label="Frosted pine branches with silver ornament, right of ticket body" style="left:220px;top:-40px;width:110px;height:140px;"></div>

  <div class="brand"><span class="dot"></span>R.L. PENROSE</div>
  <div class="raffle-title">RAFFLE TICKET</div>
  <div class="raffle-date">DEC <span class="day-badge">18</span> 2025</div>
  <div class="raffle-time">THURSDAY <span class="divider"></span> 6–10 PM</div>
  <svg class="pin" style="left:137px;top:101px" width="6" height="9" viewBox="0 0 12 16" aria-hidden="true">
    <path d="M6 0C2.7 0 0 2.6 0 5.9 0 10.3 6 16 6 16s6-5.7 6-10.1C12 2.6 9.3 0 6 0z" fill="var(--navy)"/>
  </svg>
  <div class="raffle-venue"><strong>RAVENNA BELLHAVEN</strong>318 Quillby Ave, Alderbrook<br>NJ 08219</div>

  <div class="ticket-stub">
    <div class="stub-field" style="top:22px">NAME</div>
    <div class="stub-field" style="top:38px;height:1px;padding:0"></div>
    <div class="stub-field" style="top:56px">PHONE</div>
    <div class="stub-field" style="top:75px">EMAIL</div>
    <div class="stub-field" style="top:93px">SIGN</div>
  </div>
</section>

</body>
</html>
```